INFOGRAPHIC DESING GYM SCHEDULE . FULL SCHEDULE AND CLASSES ROON SCHEDULE

I NEED TO CREATED A DESIGN FOR COMPLETE SCHEDULE TAMPLE FOR OUR GYM
AND SMALL SCHEDULE FOR EACH ROON OF THE GYM AND THE CLASSES THTA HAPPEN IN THE ROON
THE SCHEDULE WILL HAVE
CLASSES SCHEDULE
CLASSE DESCRIPTION
AND GRAPHIC EXPLAN HOW EFFECTIVE THE CLASSES ARE IN SOME IMPORT FECTOR .
I MAKE MY SELF A SAMPLE AND WILL UP LOAD IT NO WEEL DONE, BUT YOU CAN HAVE AN IDEIA
II LIKE TO MAKE IT BETTER AND MORE PROFESSIONAL .
RIGHT NOW WE CAN HAVE ALL AS PLACE HOLDER
Updates

hello i never got any other file right now i am very frustrated with this servese i spend a lot of monet for a design this experience is far from been good

Target Market(s)

gym

Font styles to use
Sans Serif

Colors
ec1f27
000000
9d9d9d

Requirements
Must have
• MUST HAVE A UNIQUE DESIGN . WILL USE ALL OF OUR GYM AND WILL NEED TO HAVE A PERSOLIZED DESIGN .
• WE NEED TO HAVE A TAMPLE WHERE WE CAN CHAGE OUR SELF BECOUSE THE CLASSE SCHEDULE CHANGE OTHER TIME
Nice to have
• THE GRAFIC EXPLAN HOW EFECTIVE THE CLASSES ARE IN EXTREMILY IMPORTANT. WE WANT TO INOVAT AND CRETED SOMETIMNH UNIQUE
• I UP LOAD OUR LOGO, IS SHOULD TO FOLOW OUR COLORS
• ON THE SCHEDUDLE SHOULD HAVE A LOGO

```html
<!DOCTYPE html>
<html lang="en">
<head>
<meta charset="utf-8">
<title>Summit Training Center – Class Schedule</title>
<link rel="stylesheet" href="https://fonts.googleapis.com/css2?family=Oswald:wght@500;600;700&family=Roboto+Condensed:ital,wght@0,400;0,700;1,400;1,700&display=swap">
<style>
  :root {
    --paper: #dfe8ef;
    --white: #ffffff;
    --ink-gray: #6d6e70;
    --rule-gray: #9d9d9d;
    --green: #3bb54a;
    --blue: #1b87c8;
    --lilac: #a469ab;
    --navy: #1d3e6c;
    --orange: #f7941d;
    --purple: #6b4e9e;
    --hiit: #5b4a9b;
    --red: #ec1f27;
    --icon-gray: #5f6062;
  }
  * { box-sizing: border-box; margin: 0; padding: 0; }
  html, body { width: 860px; height: 1200px; overflow: hidden; }
  body {
    background: var(--paper);
    font-family: "Roboto Condensed", "Arial Narrow", sans-serif;
    position: relative;
  }
  .icon { width: 24px; height: 24px; fill: currentColor; display: block; }

  /* ---------- header ---------- */
  .masthead { position: absolute; top: 0; left: 0; width: 860px; height: 160px; }
  .art {
    position: absolute; top: 14px; height: 130px; border-radius: 10px;
  }
  .art--cardio {
    left: 24px; width: 240px;
    background: linear-gradient(160deg, #e4ebf0 0%, #f2b39f 55%, #e2553b 80%, #24365f 100%);
  }
  .art--strength {
    right: 24px; width: 240px;
    background: linear-gradient(200deg, #e4ebf0 0%, #f3a38f 35%, #7fb6dd 70%, #24365f 100%);
  }
  .brand {
    position: absolute; top: 48px; left: 300px; width: 260px; height: 70px;
    display: flex; align-items: center; gap: 12px;
  }
  .brand__mark {
    width: 58px; height: 58px; border-radius: 50%;
    border: 7px solid var(--ink-gray); flex: none;
  }
  .brand__name {
    font-family: "Oswald", sans-serif; font-weight: 600; color: var(--ink-gray);
    font-size: 24px; line-height: 1.05; letter-spacing: 0.5px;
  }

  /* ---------- section titles ---------- */
  .section-title {
    position: absolute; left: 18px; right: 18px;
    display: flex; align-items: center; gap: 10px;
    font-family: "Oswald", sans-serif; font-weight: 700; color: var(--ink-gray);
    font-size: 34px; letter-spacing: 0.5px; white-space: nowrap;
  }
  .section-title::before, .section-title::after {
    content: ""; flex: 1; height: 4px; background: var(--rule-gray);
  }
  .section-title--schedule { top: 158px; }
  .section-title--definition { top: 594px; }
  .section-title--intensity { top: 880px; }

  /* ---------- schedule ---------- */
  .schedule {
    position: absolute; top: 207px; left: 14px; width: 832px;
    display: grid; grid-template-columns: repeat(6, 1fr);
    grid-template-rows: 48px repeat(4, 75px); gap: 5px;
  }
  .day {
    font-family: "Oswald", sans-serif; font-weight: 600; font-size: 23px;
    color: var(--white); display: flex; align-items: center; justify-content: center;
  }
  .day--mon { background: var(--green); }
  .day--tue { background: var(--blue); }
  .day--wed { background: var(--lilac); }
  .day--thu { background: var(--navy); }
  .day--fri { background: var(--orange); }
  .day--sat { background: var(--purple); }

  .slot {
    background: var(--white); position: relative; padding: 12px 14px 0;
    border: 2px solid #eef2f5;
  }
  .slot__time { font-style: italic; font-size: 16px; letter-spacing: -0.3px; }
  .slot .icon { position: absolute; top: 10px; right: 14px; }
  .slot__class {
    position: absolute; left: 0; right: 0; bottom: 14px; text-align: center;
    font-weight: 700; font-size: 16px; letter-spacing: -0.2px;
  }
  .is-saw { color: var(--orange); }
  .is-hiit { color: var(--hiit); }
  .is-cycle { color: var(--green); }

  /* ---------- definitions ---------- */
  .definitions {
    position: absolute; top: 652px; left: 22px; width: 816px;
    display: grid; grid-template-columns: repeat(3, 1fr); gap: 28px;
  }
  .class-card__head { display: flex; height: 42px; margin: 0 20px 0 30px; }
  .class-card__badge {
    width: 42px; background: var(--white); display: flex; align-items: center;
    justify-content: center; color: var(--icon-gray);
  }
  .class-card__name {
    flex: 1; color: var(--white); font-family: "Oswald", sans-serif; font-weight: 500;
    font-size: 22px; display: flex; align-items: center; justify-content: center;
  }
  .class-card--saw .class-card__name { background: var(--orange); }
  .class-card--hiit .class-card__name { background: var(--purple); }
  .class-card--cycle .class-card__name { background: var(--green); }
  .class-card__text {
    margin-top: 16px; background: var(--white); border-radius: 6px; height: 160px;
    padding: 12px 18px; text-align: center; font-size: 16px; line-height: 1.5;
    display: flex; align-items: center;
  }

  /* ---------- intensity ---------- */
  .legend {
    position: absolute; top: 932px; left: 0; width: 860px;
    display: flex; justify-content: center; gap: 48px;
    font-style: italic; font-size: 16px;
  }
  .legend__item { display: flex; align-items: center; gap: 10px; }
  .legend__item::before { content: ""; width: 15px; height: 15px; background: currentColor; }
  .legend__item--high { color: var(--red); }
  .legend__item--median { color: var(--orange); }
  .legend__item--low { color: var(--green); }

  .intensity {
    position: absolute; top: 966px; left: 18px; width: 824px;
    display: grid; grid-template-columns: repeat(8, 1fr);
    grid-template-rows: 42px repeat(3, 55px); gap: 4px;
  }
  .factor {
    color: var(--white); font-weight: 700; font-size: 16px;
    display: flex; align-items: center; justify-content: center;
  }
  .factor--green { background: var(--green); }
  .factor--blue { background: var(--blue); }
  .factor--lilac { background: var(--lilac); }
  .factor--navy { background: var(--navy); }
  .factor--orange { background: var(--orange); }
  .factor--purple { background: var(--purple); }
  .rating {
    background: var(--white); display: flex; flex-direction: column;
    align-items: center; justify-content: center; gap: 5px;
    font-weight: 700; font-size: 11px;
  }
  .rating .icon { width: 22px; height: 22px; }
  .high { color: var(--red); }
  .median { color: var(--orange); }
  .low { color: var(--green); }
</style>
</head>
<body>
<svg width="0" height="0" style="position:absolute" aria-hidden="true">
  <symbol id="i-kettlebell" viewBox="0 0 24 24">
    <path d="M7.5 9V6.5a4.5 4.5 0 0 1 9 0V9h-2.2V6.5a2.3 2.3 0 0 0-4.6 0V9z"/>
    <circle cx="12" cy="15" r="7.5"/>
  </symbol>
  <symbol id="i-rope" viewBox="0 0 24 24">
    <path d="M5 13V9a7 7 0 0 1 14 0v4h-2V9a5 5 0 0 0-10 0v4z"/>
    <rect x="3.5" y="13" width="5" height="9" rx="1.5"/>
    <rect x="15.5" y="13" width="5" height="9" rx="1.5"/>
  </symbol>
  <symbol id="i-heart" viewBox="0 0 24 24">
    <path d="M12 21.5 3.2 13A5.3 5.3 0 0 1 12 5.6 5.3 5.3 0 0 1 20.8 13z"/>
    <path d="M3 12.5h5l1.6-3 2.4 6 2-4.5 1.2 1.5H21" fill="none" stroke="#fff" stroke-width="1.6" stroke-linejoin="round"/>
  </symbol>
</svg>

<header class="masthead">
  <div class="art art--cardio" role="img" aria-label="Illustration of a treadmill with hanging gym rings"></div>
  <div class="brand">
    <span class="brand__mark"></span>
    <span class="brand__name">SUMMIT<br>TRAINING CENTER</span>
  </div>
  <div class="art art--strength" role="img" aria-label="Illustration of a barbell resting on a bench press rack"></div>
</header>

<h2 class="section-title section-title--schedule">SCHEDULE</h2>
<section class="schedule">
  <div class="day day--mon">MON</div>
  <div class="day day--tue">TUES</div>
  <div class="day day--wed">WED</div>
  <div class="day day--thu">THURS</div>
  <div class="day day--fri">FRI</div>
  <div class="day day--sat">SAT</div>

  <div class="slot is-saw"><span class="slot__time">8:30 am</span><svg class="icon"><use href="#i-kettlebell"/></svg><span class="slot__class">SAW</span></div>
  <div class="slot is-hiit"><span class="slot__time">8:30 am</span><svg class="icon"><use href="#i-rope"/></svg><span class="slot__class">HIIT CYCLING</span></div>
  <div class="slot is-saw"><span class="slot__time">8:30 am</span><svg class="icon"><use href="#i-kettlebell"/></svg><span class="slot__class">SAW</span></div>
  <div class="slot is-hiit"><span class="slot__time">8:30 am</span><svg class="icon"><use href="#i-rope"/></svg><span class="slot__class">HIIT CYCLING</span></div>
  <div class="slot is-saw"><span class="slot__time">8:30 am</span><svg class="icon"><use href="#i-kettlebell"/></svg><span class="slot__class">SAW</span></div>
  <div class="slot"></div>

  <div class="slot is-cycle"><span class="slot__time">9:30 am</span><svg class="icon"><use href="#i-heart"/></svg><span class="slot__class">INDOR CYCLING</span></div>
  <div class="slot is-saw"><span class="slot__time">9:30 am</span><svg class="icon"><use href="#i-kettlebell"/></svg><span class="slot__class">SAW</span></div>
  <div class="slot is-cycle"><span class="slot__time">9:30 am</span><svg class="icon"><use href="#i-heart"/></svg><span class="slot__class">INDOR CYCLING</span></div>
  <div class="slot is-saw"><span class="slot__time">9:30 am</span><svg class="icon"><use href="#i-kettlebell"/></svg><span class="slot__class">SAW</span></div>
  <div class="slot is-cycle"><span class="slot__time">9:30 am</span><svg class="icon"><use href="#i-heart"/></svg><span class="slot__class">INDOR CYCLING</span></div>
  <div class="slot is-saw"><span class="slot__time">9:30 am</span><svg class="icon"><use href="#i-kettlebell"/></svg><span class="slot__class">SAW</span></div>

  <div class="slot is-hiit"><span class="slot__time">5:30 pm</span><svg class="icon"><use href="#i-rope"/></svg><span class="slot__class">HIIT CYCLING</span></div>
  <div class="slot is-saw"><span class="slot__time">5:30 pm</span><svg class="icon"><use href="#i-kettlebell"/></svg><span class="slot__class">SAW</span></div>
  <div class="slot is-hiit"><span class="slot__time">5:30 pm</span><svg class="icon"><use href="#i-rope"/></svg><span class="slot__class">HIIT CYCLING</span></div>
  <div class="slot is-saw"><span class="slot__time">5:30 pm</span><svg class="icon"><use href="#i-kettlebell"/></svg><span class="slot__class">SAW</span></div>
  <div class="slot is-hiit"><span class="slot__time">5:30 pm</span><svg class="icon"><use href="#i-rope"/></svg><span class="slot__class">HIIT CYCLING</span></div>
  <div class="slot"></div>

  <div class="slot is-saw"><span class="slot__time">6:30 pm</span><svg class="icon"><use href="#i-kettlebell"/></svg><span class="slot__class">SAW</span></div>
  <div class="slot is-cycle"><span class="slot__time">6:30 pm</span><svg class="icon"><use href="#i-heart"/></svg><span class="slot__class">INDOR CYCLING</span></div>
  <div class="slot is-saw"><span class="slot__time">6:30 pm</span><svg class="icon"><use href="#i-kettlebell"/></svg><span class="slot__class">SAW</span></div>
  <div class="slot is-cycle"><span class="slot__time">6:30 pm</span><svg class="icon"><use href="#i-heart"/></svg><span class="slot__class">INDOR CYCLING</span></div>
  <div class="slot is-saw"><span class="slot__time">6:30 pm</span><svg class="icon"><use href="#i-kettlebell"/></svg><span class="slot__class">SAW</span></div>
  <div class="slot"></div>
</section>

<h2 class="section-title section-title--definition">CLASSES DEFINTION</h2>
<section class="definitions">
  <article class="class-card class-card--saw">
    <div class="class-card__head"><span class="class-card__badge"><svg class="icon"><use href="#i-kettlebell"/></svg></span><h3 class="class-card__name">SAW</h3></div>
    <p class="class-card__text is-saw">KIDS BOXING CLASS TEACHES BASIC BOXING SKILLS AND TECHNIQUES SUCH AS: STANCE, GUARD, MOVEMENT, JAB, CROSS, HOOK. IT INCREASE STRENGTH AND IMPROVES INDURANCE.</p>
  </article>
  <article class="class-card class-card--hiit">
    <div class="class-card__head"><span class="class-card__badge"><svg class="icon"><use href="#i-rope"/></svg></span><h3 class="class-card__name">HIIT CYCLING</h3></div>
    <p class="class-card__text is-hiit">KIDS BOXING CLASS TEACHES BASIC BOXING SKILLS AND TECHNIQUES SUCH AS: STANCE, GUARD, MOVEMENT, JAB, CROSS, HOOK. IT INCREASE STRENGTH AND IMPROVES INDURANCE.</p>
  </article>
  <article class="class-card class-card--cycle">
    <div class="class-card__head"><span class="class-card__badge"><svg class="icon"><use href="#i-heart"/></svg></span><h3 class="class-card__name">INDOR CYCLING</h3></div>
    <p class="class-card__text is-cycle">KIDS BOXING CLASS TEACHES BASIC BOXING SKILLS AND TECHNIQUES SUCH AS: STANCE, GUARD, MOVEMENT, JAB, CROSS, HOOK. IT INCREASE STRENGTH AND IMPROVES INDURANCE.</p>
  </article>
</section>

<h2 class="section-title section-title--intensity">CLASSES F INTENSITY</h2>
<div class="legend">
  <span class="legend__item legend__item--high">HIGH</span>
  <span class="legend__item legend__item--median">MEDIAN</span>
  <span class="legend__item legend__item--low">LOW</span>
</div>
<section class="intensity">
  <div class="factor factor--green">FAT BURN</div>
  <div class="factor factor--blue">INTERSNITY</div>
  <div class="factor factor--lilac">CARDIO</div>
  <div class="factor factor--navy">AGILITY</div>
  <div class="factor factor--orange">BALANCE</div>
  <div class="factor factor--purple">FLEXBILITY</div>
  <div class="factor factor--green">POWER</div>
  <div class="factor factor--blue">CONTACT</div>

  <div class="rating high"><svg class="icon"><use href="#i-kettlebell"/></svg>SAW</div>
  <div class="rating high"><svg class="icon"><use href="#i-kettlebell"/></svg>SAW</div>
  <div class="rating high"><svg class="icon"><use href="#i-kettlebell"/></svg>SAW</div>
  <div class="rating high"><svg class="icon"><use href="#i-kettlebell"/></svg>SAW</div>
  <div class="rating median"><svg class="icon"><use href="#i-kettlebell"/></svg>SAW</div>
  <div class="rating median"><svg class="icon"><use href="#i-kettlebell"/></svg>SAW</div>
  <div class="rating median"><svg class="icon"><use href="#i-kettlebell"/></svg>SAW</div>
  <div class="rating low"><svg class="icon"><use href="#i-kettlebell"/></svg>SAW</div>

  <div class="rating high"><svg class="icon"><use href="#i-rope"/></svg>HIIT CYCLING</div>
  <div class="rating high"><svg class="icon"><use href="#i-rope"/></svg>HIIT CYCLING</div>
  <div class="rating high"><svg class="icon"><use href="#i-rope"/></svg>HIIT CYCLING</div>
  <div class="rating median"><svg class="icon"><use href="#i-rope"/></svg>HIIT CYCLING</div>
  <div class="rating median"><svg class="icon"><use href="#i-rope"/></svg>HIIT CYCLING</div>
  <div class="rating median"><svg class="icon"><use href="#i-rope"/></svg>HIIT CYCLING</div>
  <div class="rating low"><svg class="icon"><use href="#i-rope"/></svg>HIIT CYCLING</div>
  <div class="rating low"><svg class="icon"><use href="#i-rope"/></svg>HIIT CYCLING</div>

  <div class="rating high"><svg class="icon"><use href="#i-heart"/></svg>INDOR CYCLING</div>
  <div class="rating median"><svg class="icon"><use href="#i-heart"/></svg>INDOR CYCLING</div>
  <div class="rating median"><svg class="icon"><use href="#i-heart"/></svg>INDOR CYCLING</div>
  <div class="rating median"><svg class="icon"><use href="#i-heart"/></svg>INDOR CYCLING</div>
  <div class="rating low"><svg class="icon"><use href="#i-heart"/></svg>INDOR CYCLING</div>
  <div class="rating low"><svg class="icon"><use href="#i-heart"/></svg>INDOR CYCLING</div>
  <div class="rating low"><svg class="icon"><use href="#i-heart"/></svg>INDOR CYCLING</div>
  <div class="rating low"><svg class="icon"><use href="#i-heart"/></svg>INDOR CYCLING</div>
</section>
</body>
</html>
```